Functional Beverage- Flavoured Vitamin Water

Hi,

We need a product label design for a new flavoured vitamin water in London: "Lumo Brisk" .

Lumo Brisk is a refreshing vitamin infusion ready to drink beverage. It is a naturally sweetened (low sugar NOT no sugar, but free from artificial sweetners), with natural colours and flavours - with added vitamins and supplements, including natural botanicals. We want to clearly label this to be a health drink and highlight the benefits. It is a STILL drink and either CLEAR or TINTED RED depending on the flavour.

We have used leading research from the nutritional industry to create functional blends in a light refreshing water that is not sugar laden or artificially flavoured. WE TASTE GREAT!

These are the 4 flavours however for the purposes of the brief I am happy for the designers to focus on either

1. CRANBERRY RASPERRY - rose red - REDOX (contains antioxidants and help immunity)
2. COCONUT PINEAPPLE - clear - BEAUTY (helps maintain hair, skin and nails)

I want the product label to be fresh and stand out as this will be facing competition from established brands (Trevanne / K-Drink).

Labels will be printed on self-adhesive plastic and be applied to a 500 ml PET clear plastic bottle. The label itself would be no more than 190mm wide by 80mm tall and will be a rectangle (to give you an idea of scale when the consumer looks at the label).

I want something as striking, pure and playful as these two brands have on their waters (but not as minimal...)

1. http://thewanderingowl.example/?p=48113
2. http://www.pelmorstudio.example/energy/arch/007215.php
3. Existing bottle is here: https://files.example/QmXpWs83

We will be relying on social media for marketing and PR so fthe design needs to transfer to that type of media well.

Thanks and good luck
Updates

Hi all,

Just a note to the invited designers - hoping some more of you can jump into the project over the weekend if you have not already submitted designs.

Thanks and regards,

Tom

Reason: Extending so we can get some more designs submitted. Thanks.

Hi,

I have increased the budget to allow for a $100 2nd prize, as we are seeing some strong designs in the closing stages.

Regards,
Tom

Reason: Collating final feedback on submissions.

Target Market(s)

18-35 yeare old professionals who consume vitamin supplements and want a ready to drink flavoured water that's different to the standard offering.

It is unisex but feel the brand may appeal more to women initially. But I dont want to disenfranchise men.

Industry/Entity Type

Marketing

Requirements
Must have
• Health benefit claims
Flavour names
Mention the natural fruit sugars and stevia
Nice to have
• Mention how it's "Low Cal not No Cal"

I like the idea of a clear or semi clear label that uses the back of the label on the opposite side like the OKRA water bottle in the attached file. This makes it looks so much more 3d than a "front" label... not a mandatory requirement - just an idea to think of.

```html
<!DOCTYPE html>
<html lang="en">
<head>
<meta charset="utf-8">
<title>Lumo Brisk – Cranberry &amp; Raspberry Label</title>
<link rel="stylesheet" href="https://fonts.googleapis.com/css2?family=Pathway+Gothic+One&display=swap">
<style>
  :root {
    --brand-red: #c4202b;
    --brand-cyan: #2bb8ea;
    --ink: #231f20;
    --panel-grey: #e6e6e7;
    --paper: #ffffff;
    --font-main: "Pathway Gothic One", "Arial Narrow", sans-serif;
  }
  * { margin: 0; padding: 0; box-sizing: border-box; }
  html, body { width: 1200px; height: 565px; overflow: hidden; background: var(--paper); }
  .label {
    position: relative;
    width: 1200px;
    height: 565px;
    font-family: var(--font-main);
    color: var(--ink);
  }
  .brand-name {
    position: absolute;
    left: 17px;
    top: 258px;
    font-size: 64px;
    line-height: 1;
    letter-spacing: 1px;
    color: var(--brand-cyan);
    text-transform: uppercase;
    white-space: nowrap;
  }
  .flavour-panel {
    position: absolute;
    left: 287px;
    top: 35px;
    width: 303px;
    height: 375px;
    background: var(--brand-red);
    color: var(--paper);
  }
  .flavour-name {
    position: absolute;
    left: 14px;
    top: 200px;
    padding-left: 10px;
    border-left: 3px solid var(--paper);
    font-weight: 400;
    font-size: 64px;
    line-height: 58px;
    text-transform: uppercase;
    white-space: nowrap;
  }
  .tagline {
    position: absolute;
    left: 32px;
    top: 329px;
    font-size: 18px;
    line-height: 20px;
    text-transform: uppercase;
    white-space: nowrap;
  }
  .edge-rule {
    position: absolute;
    left: 287px;
    top: 410px;
    width: 3px;
    height: 138px;
    background: var(--brand-red);
  }
  .benefits {
    position: absolute;
    left: 297px;
    top: 420px;
    list-style: none;
  }
  .benefits li {
    font-size: 19px;
    line-height: 24px;
    margin-bottom: 22px;
    padding-left: 6px;
    border-left: 1.5px solid var(--ink);
    text-transform: uppercase;
    white-space: nowrap;
  }
  .dot-column { position: absolute; left: 691px; top: 0; }
  .description {
    position: absolute;
    left: 603px;
    top: 214px;
    width: 306px;
    font-size: 19px;
    line-height: 23px;
    text-transform: uppercase;
    white-space: nowrap;
  }
  .description .brand-mention { text-transform: none; font-variant: small-caps; }
  .description .accent { color: var(--brand-red); }
  .nutrition-panel {
    position: absolute;
    left: 915px;
    top: 35px;
    width: 285px;
    height: 513px;
    background: var(--panel-grey);
  }
  .nutrition-note {
    position: absolute;
    left: 17px;
    top: 261px;
    font-size: 18px;
    text-transform: uppercase;
    white-space: nowrap;
    color: #333;
  }
</style>
</head>
<body>
<main class="label">
  <div class="brand-name">Lumo Brisk</div>

  <section class="flavour-panel">
    <h1 class="flavour-name">Cranberry &amp;<br>Raspberry</h1>
    <p class="tagline">A refreshing vitamin infused beverage</p>
  </section>
  <div class="edge-rule"></div>

  <ul class="benefits">
    <li>Contains antioxidants</li>
    <li>Vitamin and supplement infused</li>
    <li>Naturally sweetened</li>
  </ul>

  <svg class="dot-column" width="64" height="565" viewBox="0 0 64 565" aria-hidden="true">
    <g fill="var(--brand-red)">
      <circle cx="32" cy="16" r="6"/>
      <circle cx="32" cy="85" r="9"/>
      <circle cx="32" cy="124" r="15"/>
      <circle cx="32" cy="178" r="21"/>
      <circle cx="32" cy="409" r="21"/>
      <circle cx="32" cy="462" r="16"/>
      <circle cx="32" cy="504" r="11"/>
      <circle cx="32" cy="537" r="7"/>
    </g>
  </svg>

  <p class="description">
    <span class="brand-mention">Lumo Brisk</span> <span class="accent">Cranberry &amp; Rasberry</span> is a<br>
    naturally sweetened, low sugar<br>
    vitamin drink containing natural colours<br>
    and flavours, with added vitamins and<br>
    supplements including natural botanicals.<br>
    This is a low cal, <span class="accent">not</span> no cal drink to<br>
    ensure your body gets the natural sugars<br>
    it requires.
  </p>

  <aside class="nutrition-panel">
    <p class="nutrition-note">Space for nutrition information etc</p>
  </aside>
</main>
</body>
</html>
```